Voice agent website redesign, responsive. Current website functional, needs fresh look.

** updated 01/04/2015 ** Stock photos and video OK
TQ Sounds is redesigning their website to refresh the look and feel and also to make the website more useable in portable devices.
We also intend to replace our existing iPhone app with responsive HTML.
We want to keep the features but update the way they are displayed.
The current website is at: http://www.tqsounds-demo.com.au. (examples of important pages are in the attachments)
The current website is written in .NET and MS SQL but designs optimised for WordPress will also be accepted.
We have corporate colours and a logo
We want a dynamic element on the front page
We do not mind the idea of a slider, but I must be modern and capable of video backgrounds
We like the clean design of our main competitor: http://www.zelvar-demo.com.au but the site is busy and not responsive.
The site must be designed to use responsive HTML and be easy to see and navigate using smaller viewports.
Once awarded the contract the designer must supply 4 pages in 3 formats, for which we will pay an extra $80, as outlined below:
Submission for selection
Designs must be submitted for selection with 1 required page (home page) in 1 required resolution and 1 optional resolution;
Versions:
• (Required) Full page web landscape – 1920 x 1080
• (Optional) Low resolution portrait (e.g. iPhone 3/4) – 320 x 480
Submission required when awarded
Final supplied designs must have 3 versions of 4 required pages as layered Photoshop files;
Versions:
• Full page web landscape – 1920 x 1080
• Medium resolution landscape (e.g. iPad) – 1024 x 768
• Low resolution portrait (e.g. iPhone 3/4) – 320 x 480
Pages:
• home page
• generic template
• search results
• talent page
The designer may also offer to convert the site into HTML and CSS for an added fee.
The attachments supplied contains important features like site menu and required elements, but only guidelines to design.
Please do read carefully for details on required elements, but do feel free to change the design, look and feel completely.
Attached are;
Target Market(s)
Advertising agencies who hire voice artists, also a showcase for the artists themselves
Look and feel

```html
<!DOCTYPE html>
<html lang="en">
<head>
<meta charset="utf-8">
<title>TQ Sounds – Home</title>
<link href="https://fonts.googleapis.com/css2?family=Lato:wght@400;700&display=swap" rel="stylesheet">
<style>
:root{
  --green:#8cc43f;
  --green-dark:#76ad2c;
  --topbar:#535353;
  --ink:#222;
  --text:#555;
  --white:#fff;
  --footer:#0d0f0c;
}
*{margin:0;padding:0;box-sizing:border-box}
html,body{width:748px;height:1200px;overflow:hidden}
body{position:relative;font-family:'Lato',sans-serif;background:var(--white);color:var(--text)}
.abs{position:absolute}

/* top bar */
.topbar{left:0;top:0;width:748px;height:23px;background:var(--topbar);color:#eee;font-size:6.5px}
.topbar .phone{top:7px;display:flex;align-items:center;gap:4px}
.topbar .social{top:8px;width:7px;height:7px;border-radius:50%;background:#ddd}

/* nav */
.nav{left:0;top:23px;width:748px;height:66px;background:var(--green)}
.brand{left:115px;top:22px;display:flex;align-items:center;gap:6px;color:var(--white);font-weight:700;font-size:15px;letter-spacing:.5px}
.brand .mark{width:12px;height:12px;background:var(--white)}
.menu a{position:absolute;top:30px;transform:translateX(-50%);color:var(--white);font-size:6.5px;font-weight:700;text-decoration:none;letter-spacing:.2px}
.menu .active{top:0;left:289px;width:37px;height:66px;background:var(--white);transform:none}
.menu .active span{position:absolute;left:50%;top:30px;transform:translateX(-50%);color:var(--green)}

/* hero */
.hero{left:0;top:89px;width:748px;height:377px;background:radial-gradient(circle at 28% 8%,#e8a24a 0,#a24c14 18%,transparent 40%),radial-gradient(circle at 62% 45%,#c76a28 0,#5a2208 35%,transparent 60%),linear-gradient(90deg,#2a0e05,#4a1b08 50%,#241007)}
.hero-title{left:115px;top:143px;font-size:21px;color:var(--white);letter-spacing:-.3px}
.hero-title em{font-style:normal;color:var(--green)}
.search{left:115px;top:172px;width:207px;height:236px;background:var(--green)}
.search label{position:absolute;color:var(--white);font-size:6.5px}
.select{position:absolute;height:21px;border:1px solid #d9ecbf;background:#99cc52;color:var(--white);font-size:5.5px;padding-left:7px;line-height:19px}
.select .arrow{position:absolute;right:2px;top:2px;width:16px;height:15px;background:var(--white);display:flex;align-items:center;justify-content:center}
.btn-light{position:absolute;top:193px;height:25px;background:var(--white);color:var(--green);font-size:7px;font-weight:700;display:flex;align-items:center;justify-content:center}

/* about */
.about-photo{left:115px;top:499px;width:252px;height:184px;background:linear-gradient(180deg,#d9dfe6 0,#e8e9e6 45%,#b7a27a 70%,#8c7752 100%)}
.h2{position:absolute;font-size:14.5px;color:var(--ink);letter-spacing:-.2px;white-space:nowrap}
.h2 em{font-style:normal;color:var(--green)}
.h2 .rule{position:absolute;left:0;right:0;top:19px;height:1px;background:var(--ink)}
.about-text{left:381px;top:534px;width:252px;font-size:6.1px;line-height:10.3px;text-align:justify;color:#555}
.about-text p+p{margin-top:10px}
.btn-green{left:381px;top:662px;width:75px;height:21px;background:var(--green);color:var(--white);font-size:6.5px;font-weight:700;display:flex;align-items:center;justify-content:center;gap:4px}
.divider{left:115px;top:709px;width:518px;height:1px;background:#e6e6e6}

/* services */
.services{left:115px;top:758px;list-style:none;font-size:6.2px;color:var(--ink)}
.services li{position:relative;padding-left:10px;height:11.3px;line-height:11.3px;width:84px}
.services li::before{content:"";position:absolute;left:0;top:3px;width:6px;height:6px;border-radius:50%;background:var(--green)}
.services li.wrap{height:auto;line-height:11.3px}

/* recent work */
.video{top:771px;width:207px;height:118px;background:#111}
.video .frame{position:absolute;left:0;top:7px;width:207px;height:100px}
.video .bar{position:absolute;left:0;bottom:0;width:207px;height:11px;background:#1c1c1c;border-top:2px solid #555}
.video .play{position:absolute;left:50%;top:50%;transform:translate(-50%,-60%)}
.pager{top:903px;width:22px;height:22px;background:var(--green);display:flex;align-items:center;justify-content:center}

/* footer */
.footer{left:0;top:957px;width:748px;height:243px;background:radial-gradient(ellipse at 30% 25%,#3a3d33 0,#1a1c17 35%,transparent 60%),radial-gradient(ellipse at 80% 60%,#2a2c25 0,transparent 45%),var(--footer)}
.fcol{top:1003px;width:170px;text-align:center;color:var(--white);font-size:9px;line-height:14.2px}
.fcol svg{display:block;margin:0 auto 9px}
.copy{left:0;top:1134px;width:748px;text-align:center;color:#eee;font-size:5.6px}
.fsocial{top:1152px;width:20px;height:20px;border-radius:50%;border:1px solid #aaa}
.fsocial.on{background:var(--white);border-color:var(--white)}
</style>
</head>
<body>

<div class="abs topbar">
  <div class="abs phone" style="left:115px"><svg width="6" height="6" viewBox="0 0 10 10"><path d="M2 0l2 2-1 1.5c.6 1.4 2 2.8 3.5 3.5L8 6l2 2-1.5 2C4 10 0 6 0 1.5z" fill="#eee"/></svg>+61 2 5550 1840</div>
  <div class="abs phone" style="left:204px"><svg width="6" height="6" viewBox="0 0 10 10"><path d="M2 0l2 2-1 1.5c.6 1.4 2 2.8 3.5 3.5L8 6l2 2-1.5 2C4 10 0 6 0 1.5z" fill="#eee"/></svg>+61 3 5550 2963</div>
  <span class="abs social" style="left:583px"></span>
  <span class="abs social" style="left:604px"></span>
  <span class="abs social" style="left:626px"></span>
</div>

<header class="abs nav">
  <div class="abs brand"><span class="mark"></span>TQ SOUNDS</div>
  <nav class="menu">
    <a class="active" href="#"><span>HOME</span></a>
    <a href="#" style="left:354px">RATES</a>
    <a href="#" style="left:407px">ABOUT US</a>
    <a href="#" style="left:458px">FAQS</a>
    <a href="#" style="left:511px">PAYMENTS</a>
    <a href="#" style="left:565px">LOGIN</a>
    <a href="#" style="left:617px">CONTACT</a>
  </nav>
</header>

<section class="abs hero" role="img" aria-label="Close-up of a vintage chrome studio microphone against warm blurred stage lights"></section>
<h1 class="abs hero-title" style="font-weight:400">JUST <em>SAY</em> THE <em>WORD</em>.</h1>

<form class="abs search">
  <label style="left:17px;top:18px">Search By Name</label>
  <div class="select" style="left:17px;top:29px;width:173px">Please Select :<span class="arrow"><svg width="7" height="5" viewBox="0 0 7 5"><path d="M1 1l2.5 2.5L6 1" stroke="#8cc43f" stroke-width="1.4" fill="none"/></svg></span></div>

  <label style="left:17px;top:62px">Location</label>
  <label style="left:106px;top:62px">Sex</label>
  <div class="select" style="left:17px;top:73px;width:83px">ANY<span class="arrow"><svg width="7" height="5" viewBox="0 0 7 5"><path d="M1 1l2.5 2.5L6 1" stroke="#8cc43f" stroke-width="1.4" fill="none"/></svg></span></div>
  <div class="select" style="left:106px;top:73px;width:84px">ANY<span class="arrow"><svg width="7" height="5" viewBox="0 0 7 5"><path d="M1 1l2.5 2.5L6 1" stroke="#8cc43f" stroke-width="1.4" fill="none"/></svg></span></div>

  <label style="left:17px;top:105px">Voice Type</label>
  <label style="left:106px;top:105px">Age</label>
  <div class="select" style="left:17px;top:116px;width:83px">ANY<span class="arrow"><svg width="7" height="5" viewBox="0 0 7 5"><path d="M1 1l2.5 2.5L6 1" stroke="#8cc43f" stroke-width="1.4" fill="none"/></svg></span></div>
  <div class="select" style="left:106px;top:116px;width:84px">ANY<span class="arrow"><svg width="7" height="5" viewBox="0 0 7 5"><path d="M1 1l2.5 2.5L6 1" stroke="#8cc43f" stroke-width="1.4" fill="none"/></svg></span></div>

  <label style="left:17px;top:149px">Language</label>
  <label style="left:106px;top:149px">Accent</label>
  <div class="select" style="left:17px;top:160px;width:83px">ANY<span class="arrow"><svg width="7" height="5" viewBox="0 0 7 5"><path d="M1 1l2.5 2.5L6 1" stroke="#8cc43f" stroke-width="1.4" fill="none"/></svg></span></div>
  <div class="select" style="left:106px;top:160px;width:84px">ANY<span class="arrow"><svg width="7" height="5" viewBox="0 0 7 5"><path d="M1 1l2.5 2.5L6 1" stroke="#8cc43f" stroke-width="1.4" fill="none"/></svg></span></div>

  <div class="btn-light" style="left:45px;width:57px">VIEW ALL</div>
  <div class="btn-light" style="left:107px;width:56px">SEARCH</div>
</form>

<div class="abs about-photo" role="img" aria-label="Young woman with a guitar sitting on a suitcase in an open countryside field"></div>
<h2 class="h2" style="left:381px;top:496px;font-weight:400">ABOUT <em>TQ</em> SOUNDS<span class="rule"></span></h2>
<div class="abs about-text">
  <p>TQ Sounds is one of Australia’s most successful voice over artists’ agencies. It has long been established as a friendly, professional and high quality Australian agency that has a singular focus on the business of voice overs. The company represents over 120 of Australia’s most exceptional voice artists as well as high profile actors across a wide range of styles, ages, accents, characters and foreign languages.</p>
  <p>The management team of Rowan Kettle, Mira Dalbeck and Sana Orvell supported by Managing Director Felix Harwood and accounts manager Ines Varkonyi all live and breathe voice overs. They are not distracted by repping anyone other than talented, professional voice overs artists. TQ Sounds staff understand the field intimately and service hundreds of customers in a friendly and constructive manner every day.</p>
</div>
<div class="abs btn-green">LEARN MORE <svg width="7" height="7" viewBox="0 0 10 10"><circle cx="5" cy="5" r="5" fill="#fff"/><path d="M4 2.8L6.2 5 4 7.2" stroke="#8cc43f" stroke-width="1.5" fill="none"/></svg></div>

<div class="abs divider"></div>

<h2 class="h2" style="left:115px;top:726px;font-weight:400"><em>OUR</em> SERVICE<span class="rule" style="right:0"></span></h2>
<ul class="abs services">
  <li>Broadcast Advertising</li>
  <li>TV and Radio Imaging</li>
  <li>Promotions</li>
  <li>IVR</li>
  <li>Messages on Hold</li>
  <li>Documentary narration</li>
  <li>Website presentation</li>
  <li>Corporate</li>
  <li>Multi-media</li>
  <li>Animation</li>
  <li>Computer Games</li>
  <li>Character Voices</li>
  <li>Foreign Language</li>
  <li class="wrap">Every conceivable voice type and usage</li>
</ul>

<h2 class="h2" style="left:373px;top:725px;font-weight:400"><em>RECENT</em> WORK<span class="rule"></span></h2>

<div class="abs video" style="left:204px">
  <div class="frame" role="img" aria-label="Video still of a singer performing on a blue-lit stage" style="background:linear-gradient(135deg,#1d3f8a,#3b5fb0 45%,#0e1d45)"></div>
  <svg class="play" width="22" height="22" viewBox="0 0 22 22"><circle cx="11" cy="11" r="11" fill="rgba(0,0,0,.6)"/><path d="M8.5 6.5l7 4.5-7 4.5z" fill="#fff"/></svg>
  <div class="bar"></div>
</div>
<div class="abs video" style="left:426px">
  <div class="frame" role="img" aria-label="Video still of a singer holding a vintage microphone" style="background:linear-gradient(135deg,#e7d6c2,#b98a62 50%,#6e4a30)"></div>
  <svg class="play" width="22" height="22" viewBox="0 0 22 22"><circle cx="11" cy="11" r="11" fill="rgba(0,0,0,.6)"/><path d="M8.5 6.5l7 4.5-7 4.5z" fill="#fff"/></svg>
  <div class="bar"></div>
</div>
<div class="abs pager" style="left:389px"><svg width="6" height="8" viewBox="0 0 6 8"><path d="M5 1L2 4l3 3" stroke="#fff" stroke-width="1.3" fill="none"/></svg></div>
<div class="abs pager" style="left:426px"><svg width="6" height="8" viewBox="0 0 6 8"><path d="M1 1l3 3-3 3" stroke="#fff" stroke-width="1.3" fill="none"/></svg></div>

<footer class="abs footer" role="img" aria-label="Dark background photograph of vintage studio microphones"></footer>
<div class="abs fcol" style="left:111px;text-align:left;padding-left:43px">
  <svg width="11" height="11" viewBox="0 0 10 10" style="margin:0 0 9px 37px"><path d="M2 0l2 2-1 1.5c.6 1.4 2 2.8 3.5 3.5L8 6l2 2-1.5 2C4 10 0 6 0 1.5z" fill="#fff"/></svg>
  PH +61 2 5550 1840<br>PH +61 3 5550 2963<br>FN +61 2 5550 1877
</div>
<div class="abs fcol" style="left:289px">
  <svg width="12" height="9" viewBox="0 0 12 9"><rect x=".6" y=".6" width="10.8" height="7.8" fill="none" stroke="#fff" stroke-width="1.1"/><path d="M.8 1l5.2 4 5.2-4" stroke="#fff" stroke-width="1.1" fill="none"/></svg>
  felix@tqsounds-demo.com.au<br>accounts@tqsounds-demo.com.au<br>nell@tqsounds-demo.com.au
</div>
<div class="abs fcol" style="left:467px">
  <svg width="9" height="12" viewBox="0 0 9 12"><path d="M4.5 0A4.5 4.5 0 0 0 0 4.5C0 8 4.5 12 4.5 12S9 8 9 4.5A4.5 4.5 0 0 0 4.5 0z" fill="#fff"/><circle cx="4.5" cy="4.5" r="1.7" fill="#111"/></svg>
  TQ Sounds Pty Limited<br>Suite 14, 57 Harlow St<br>Marrick Junction NSW 2099<br>Australia
</div>
<p class="abs copy">© Copyright 2015 TQ Sounds Pty Limited &nbsp;|&nbsp; Privacy Policy &amp; Terms and Conditions</p>
<span class="abs fsocial on" style="left:314px"></span>
<span class="abs fsocial" style="left:339px"></span>
<span class="abs fsocial" style="left:364px"></span>
<span class="abs fsocial" style="left:389px"></span>
<span class="abs fsocial" style="left:414px"></span>

</body>
</html>
```